KRV Anti-Money Laundering Postcard

We are a U.S. based regulatory compliance consulting company who services the financial industry (stock, bonds, equities, banking, etc.)

One of the services that we offer is Independent Anti-Money Laundering audit reviews. These reviews are required by U.S. law for certain financial institutions.

We are looking for a 6" x 8.5" horizontally oriented postcard to market our services in this business. The card should be sharp and professional.

The font and back of the card must have our logo and include

"Anti-Money Laundering Compliance" or "Anti-Money Laundering Compliance Services"

We would like the following message to be included on the card either on the front or preferably the back:

"Belwick & Associates are specialists in Anti-Money Laundering compliance. Our firm’s Anti-Money Laundering compliance solutions include:

• Independent Money Laundering Audits
• Anti-Money Laundering Compliance Procedures
• Anti-Money Laundering Training

Let our expert compliance team assist you in ensuring that your firm is compliant with all of its money laundering and other compliance obligations.

The back of the card should have our address, website, phone number and website: The address is normally included in the return address section noted in the Post Office requirements section blow.

42 W. Calloway Street, Suite 300
Pasadena, CA 91101
(877) 318-4092
info@belwickandassociates.example
www.belwickandassociates.example

Back of the postcard Post Office Design requirements:

http://www.quillmailprint.example/products/postcard-deluxe

Target Market(s)

Stock Brokerage Firms, Investment Advisers, Banks and other financial institutions

Industry/Entity Type

Financial Planning

Font styles to use
Sans Serif

Requirements
Must have
• Our Logo on the front and back. Clean and professional. Nice artwork.

```html
<!DOCTYPE html>
<html lang="en">
<head>
<meta charset="utf-8">
<title>Belwick &amp; Associates – Anti-Money Laundering Postcard</title>
<link rel="stylesheet" href="https://fonts.googleapis.com/css2?family=Cinzel:wght@600;700&family=Open+Sans:wght@400;600&display=swap">
<style>
  :root {
    --red: #e31e26;
    --black: #0b0b0b;
    --card: #f1f1f2;
    --grey: #a7a8aa;
    --grey-light: #cfd0d2;
    --ink: #231f20;
    --logo-ink: #3a3a3c;
    --white: #ffffff;
  }
  * { box-sizing: border-box; margin: 0; padding: 0; }
  html, body { width: 878px; height: 1200px; overflow: hidden; background: var(--white); }
  body { position: relative; font-family: "Open Sans", Arial, sans-serif; color: var(--ink); }

  .postcard { position: absolute; left: 79px; width: 710px; background: var(--card); overflow: hidden; }
  .postcard--front { top: 70px; height: 502px; }
  .postcard--back { top: 628px; height: 522px; }

  .brand { position: absolute; display: flex; align-items: center; gap: 12px; }
  .brand__mark { width: 34px; height: 34px; background: var(--red); }
  .brand__name {
    font-family: "Cinzel", Georgia, serif; font-weight: 700; font-size: 30px;
    letter-spacing: 1px; color: var(--logo-ink); line-height: 1; white-space: nowrap;
  }
  .postcard--front .brand { left: 44px; top: 38px; }
  .postcard--back .brand { left: 52px; top: 326px; }

  .title {
    font-family: "Cinzel", Georgia, serif; font-weight: 700; color: var(--white);
    text-transform: uppercase; letter-spacing: .5px; white-space: nowrap;
  }
  .title-bar {
    position: absolute; left: 41px; top: 125px; width: 608px; height: 40px; z-index: 2;
    background: var(--red); display: flex; align-items: center; justify-content: center;
    font-size: 18px;
  }
  .black-band { position: absolute; left: 0; top: 144px; width: 710px; height: 234px; background: var(--black); }

  .message { position: absolute; font-size: 12.6px; line-height: 17px; }
  .message p { margin-bottom: 17px; }
  .message ul { list-style: none; margin-bottom: 17px; }
  .message li::before { content: "• "; }
  .postcard--front .message { left: 41px; top: 170px; width: 620px; color: var(--white); z-index: 2; }
  .postcard--back .message { left: 60px; top: 102px; width: 620px; color: var(--ink); }

  .contact-band {
    position: absolute; left: 0; top: 378px; width: 710px; height: 80px;
    background: var(--red); color: var(--white); font-size: 12.6px;
  }
  .contact-band__address { position: absolute; top: 10px; width: 100%; text-align: center; }
  .contact-band__row { position: absolute; top: 31px; left: 47px; right: 50px; display: flex; justify-content: space-between; }

  .swoosh { position: absolute; left: 0; display: block; }
  .postcard--front .swoosh { top: 458px; }
  .postcard--back .swoosh { top: 472px; }

  .back-header {
    position: absolute; left: 0; top: 0; width: 710px; height: 88px; background: var(--red);
    display: flex; align-items: center; padding-left: 60px; font-size: 21px;
  }
  .back-contact { position: absolute; left: 50px; top: 391px; font-size: 11px; color: var(--ink); white-space: nowrap; }
  .web-strip { position: absolute; left: 0; top: 416px; display: block; }
  .web-strip__url {
    position: absolute; left: 430px; top: 427px; font-size: 12.5px; letter-spacing: 1.2px;
    color: var(--white); white-space: nowrap;
  }
</style>
</head>
<body>

<section class="postcard postcard--front">
  <div class="brand">
    <span class="brand__mark"></span>
    <span class="brand__name">Belwick &amp; Associates</span>
  </div>
  <h1 class="title title-bar">Anti-Money Laundering Compliance Services</h1>
  <div class="black-band"></div>
  <div class="message">
    <p>Belwick &amp; Associates are specialists in Anti-Money Laundering compliance. Our firm’s Anti-Money Laundering compliance solutions include:</p>
    <ul>
      <li>Independent Money Laundering Audits</li>
      <li>Anti-Money Laundering Compliance Procedures</li>
      <li>Anti-Money Laundering Training</li>
    </ul>
    <p>Let our expert compliance team assist you in ensuring that your firm is compliant with all of its money laundering and other compliance obligations.</p>
    <p>The back of the card should have our address, website, phone number and website: The address is normally included in the return address section noted in the Post Office requirements section blow.</p>
  </div>
  <div class="contact-band">
    <div class="contact-band__address">42 W. Calloway Street, Suite 300 Pasadena, CA 91101</div>
    <div class="contact-band__row">
      <span>(877) 318-4092</span>
      <span>info@belwickandassociates.example</span>
      <span>www.belwickandassociates.example</span>
    </div>
  </div>
  <svg class="swoosh" width="710" height="44" viewBox="0 0 710 44">
    <rect width="710" height="44" fill="var(--grey-light)"/>
    <path d="M0 44 Q355 -6 710 44 Z" fill="var(--white)"/>
  </svg>
</section>

<section class="postcard postcard--back">
  <h2 class="title back-header">Anti-Money Laundering Compliance Services</h2>
  <div class="message">
    <p>Belwick &amp; Associates are specialists in Anti-Money Laundering compliance. Our firm’s Anti-Money Laundering compliance solutions include:</p>
    <ul>
      <li>Independent Money Laundering Audits</li>
      <li>Anti-Money Laundering Compliance Procedures</li>
      <li>Anti-Money Laundering Training</li>
    </ul>
    <p>Let our expert compliance team assist you in ensuring that your firm is compliant with all of its money laundering and other compliance obligations.</p>
    <p>The back of the card should have our address, website, phone number and website: The address is normally included in the return address section noted in the Post Office requirements section blow.</p>
  </div>
  <div class="brand">
    <span class="brand__mark"></span>
    <span class="brand__name">Belwick &amp; Associates</span>
  </div>
  <div class="back-contact">42 W. Calloway Street, Suite 300 Pasadena, CA 91101 | (877) 318-4092 &nbsp;| &nbsp;info@belwickandassociates.example</div>
  <svg class="web-strip" width="710" height="40" viewBox="0 0 710 40">
    <polygon points="0,13 409,13 401,30 0,30" fill="var(--grey)"/>
    <polygon points="414,0 710,0 710,40 394,40" fill="var(--red)"/>
  </svg>
  <div class="web-strip__url">www.belwickandassociates.example</div>
  <svg class="swoosh" width="710" height="50" viewBox="0 0 710 50">
    <rect width="710" height="50" fill="var(--grey-light)"/>
    <path d="M0 50 Q355 -6 710 50 Z" fill="var(--white)"/>
  </svg>
</section>

</body>
</html>
```